Bramble Peak Information Technology Business Card
Services for Move Add Change, Technical Relocation, Server Room Support, Technical Support
Bramble Peak Information Technology Business Card - Information Technology
Creative Brief
Professional
Owen Darlisk
2917 41st Lane Northeast Seattle WA 98422
owen@bramblepkit-example.com
www.bramblepkit-example.com
The original logo on the back, #34 and #35
Move Add and Changes, Corporate Relocation, Server Room Support, Technical Support

```html
<!DOCTYPE html>
<html lang="en">
<head>
<meta charset="utf-8">
<title>Bramble Peak Information Technology Business Card</title>
<link href="https://fonts.googleapis.com/css2?family=Michroma&family=Open+Sans:wght@400;600&display=swap" rel="stylesheet">
<style>
  :root {
    --bg: #e6e6e6;
    --card-top: #ffffff;
    --card-bottom: #ececec;
    --ink: #3a3b3d;
    --band: #444548;
    --accent: #f39a1e;
    --muted: #6c6d70;
  }
  * { margin: 0; padding: 0; box-sizing: border-box; }
  html, body { width: 1200px; height: 901px; overflow: hidden; background: var(--bg); }
  .canvas { position: relative; width: 1200px; height: 901px; }
  .card {
    position: absolute; left: 75px; top: 150px; width: 1050px; height: 600px;
    border-radius: 44px; overflow: hidden;
    background: linear-gradient(180deg, var(--card-top) 0%, var(--card-bottom) 100%);
    box-shadow: 0 12px 40px rgba(0,0,0,0.18);
  }
  .wave-area {
    position: absolute; left: 0; right: 0; bottom: 0; height: 150px;
    background: linear-gradient(180deg, rgba(243,154,30,0) 0%, rgba(243,154,30,0.55) 25%, #6a5a48 55%, var(--band) 80%);
  }
  .contacts {
    position: absolute; left: 70px; top: 150px; list-style: none;
    font-family: "Open Sans", sans-serif; font-size: 18px; color: var(--muted);
  }
  .contacts li { display: flex; align-items: center; height: 36px; }
  .contacts svg { width: 18px; height: 18px; margin-right: 14px; fill: var(--accent); }
  .brand {
    position: absolute; left: 470px; top: 240px; display: flex; align-items: center;
    font-family: "Michroma", sans-serif; font-size: 38px; color: var(--ink); letter-spacing: 1px;
  }
  .brand-dot { width: 18px; height: 18px; border-radius: 50%; background: var(--accent); margin-right: 14px; }
  .person {
    position: absolute; right: 118px; top: 318px; text-align: right;
    font-family: "Michroma", sans-serif;
  }
  .person-name { font-size: 19px; color: var(--accent); letter-spacing: 1px; }
  .person-role { font-size: 15px; color: var(--ink); margin-top: 6px; letter-spacing: 1px; }
</style>
</head>
<body>
<div class="canvas">
  <div class="card">
    <div class="wave-area" role="img" aria-label="Decorative orange and dark grey wave across the bottom of the card"></div>

    <ul class="contacts">
      <li><svg viewBox="0 0 20 20"><path d="M5 2l3 4-2 2c1 3 3 5 6 6l2-2 4 3-2 3C9 18 2 11 2 4z"/></svg>012 345 6789</li>
      <li><svg viewBox="0 0 20 20"><rect x="5" y="1" width="10" height="18" rx="2"/></svg>012 345 6789</li>
      <li><svg viewBox="0 0 20 20"><rect x="2" y="7" width="16" height="10" rx="1"/><rect x="5" y="2" width="10" height="6"/></svg>012 345 6789</li>
      <li><svg viewBox="0 0 20 20"><path d="M1 4h18v12H1z M1 4l9 7 9-7"/></svg>owen@bramblepkit-example.com</li>
      <li><svg viewBox="0 0 20 20"><circle cx="10" cy="10" r="9"/></svg>www.bramblepkit-example.com</li>
    </ul>

    <div class="brand"><span class="brand-dot"></span>BRAMBLE PEAK</div>

    <div class="person">
      <div class="person-name">OWEN DARLISK</div>
      <div class="person-role">FINANCIAL ADVISOR</div>
    </div>
  </div>
</div>
</body>
</html>
```